Velmorans Business Card

Business card for philanthropic organization

Industry/Entity Type

Business

Contact Information for Business Card

Need a very ELEGANT, sober, embossed, formal business card... it should transmit CREDIBILITY. Not looking for a "fun card". would like white, grays or black designs.

Font styles to use
Script

Requirements
Must have
• Embossed look

```html
<!DOCTYPE html>
<html lang="en">
<head>
<meta charset="UTF-8">
<title>Velmorans Business Card</title>
<link href="https://fonts.googleapis.com/css2?family=Great+Vibes&family=Alegreya+Sans:ital,wght@0,400;1,400;1,500&display=swap" rel="stylesheet">
<style>
  :root {
    --page-bg: #d9d9d9;
    --card-top: #3c3c3c;
    --card-mid: #1f1f1f;
    --card-bottom: #050505;
    --band: rgba(255,255,255,0.07);
    --silver-light: #ffffff;
    --silver-dark: #8c8c8c;
    --text-light: #ececec;
    --text-soft: #d6d6d6;
    --mark-fill: #cfcfcf;
    --icon-face: #e6e6e6;
    --icon-shade: #9a9a9a;
    --icon-ink: #1a1a1a;
  }
  html, body {
    margin: 0;
    width: 1200px;
    height: 1000px;
    overflow: hidden;
    background: var(--page-bg);
  }
  .business-card {
    position: absolute;
    left: 75px;
    top: 200px;
    width: 1050px;
    height: 600px;
    background:
      radial-gradient(ellipse 70% 55% at 70% 25%, rgba(255,255,255,0.06), transparent 70%),
      linear-gradient(180deg, var(--card-top) 0%, var(--card-mid) 45%, var(--card-bottom) 100%);
    box-shadow: 0 2px 4px rgba(0,0,0,0.3);
    overflow: hidden;
    font-family: "Alegreya Sans", sans-serif;
  }
  .name-band {
    position: absolute;
    left: 0;
    top: 37px;
    width: 780px;
    height: 123px;
    background: var(--band);
  }
  .member-name {
    position: absolute;
    left: 24px;
    top: 10px;
    margin: 0;
    font-family: "Great Vibes", cursive;
    font-weight: 400;
    font-size: 116px;
    line-height: 1.2;
    white-space: nowrap;
    background: linear-gradient(180deg, var(--silver-light) 20%, var(--silver-dark) 90%);
    -webkit-background-clip: text;
    background-clip: text;
    color: transparent;
    filter: drop-shadow(1px 2px 1px rgba(0,0,0,0.8));
  }
  .temple-name, .office-title {
    position: absolute;
    left: 38px;
    margin: 0;
    font-style: italic;
    text-transform: uppercase;
    white-space: nowrap;
    text-shadow: 1px 1px 1px rgba(0,0,0,0.7);
  }
  .temple-name {
    top: 172px;
    font-size: 40px;
    font-weight: 500;
    color: var(--text-light);
  }
  .office-title {
    top: 232px;
    font-size: 38px;
    font-weight: 400;
    color: var(--text-soft);
  }
  .org-mark {
    position: absolute;
    left: 790px;
    top: 60px;
    width: 220px;
    display: flex;
    flex-direction: column;
    align-items: center;
    gap: 16px;
    font-size: 40px;
    color: var(--text-light);
  }
  .org-mark-dot {
    width: 120px;
    height: 120px;
    border-radius: 50%;
    background: var(--mark-fill);
  }
  .postal-address {
    position: absolute;
    left: 38px;
    top: 398px;
    margin: 0;
    font-style: normal;
    font-size: 39px;
    line-height: 60px;
    color: var(--text-light);
  }
  .contact-row {
    position: absolute;
    left: 22px;
    top: 530px;
    display: flex;
    align-items: center;
    font-size: 37px;
    color: var(--text-light);
  }
  .contact-item {
    display: flex;
    align-items: center;
    gap: 20px;
  }
  .phone-item { width: 485px; }
  .contact-icon { width: 56px; height: 56px; }
</style>
</head>
<body>
  <main class="business-card">
    <div class="name-band"></div>
    <h1 class="member-name">Leandro Valcarce</h1>
    <p class="temple-name">Amar Selim Velmorans</p>
    <p class="office-title">Potentate 2017</p>

    <div class="org-mark">
      <span class="org-mark-dot"></span>
      <span>Velmorans</span>
    </div>

    <address class="postal-address">
      P.O. Box 0831-07215<br>
      Panama, Republic of Panama
    </address>

    <div class="contact-row">
      <div class="contact-item phone-item">
        <svg class="contact-icon" viewBox="0 0 56 56" aria-hidden="true">
          <polygon points="28,2 54,28 28,54 2,28" fill="var(--icon-face)"/>
          <polygon points="28,2 54,28 28,28" fill="var(--icon-shade)"/>
          <rect x="20" y="13" width="16" height="30" rx="3" fill="var(--icon-ink)"/>
          <rect x="22.5" y="17" width="11" height="20" fill="var(--icon-face)"/>
          <circle cx="28" cy="40" r="1.6" fill="var(--icon-face)"/>
        </svg>
        <span>+(507)-6240-3187</span>
      </div>
      <div class="contact-item">
        <svg class="contact-icon" viewBox="0 0 56 56" aria-hidden="true">
          <polygon points="28,2 54,28 28,54 2,28" fill="var(--icon-face)"/>
          <polygon points="28,2 54,28 28,28" fill="var(--icon-shade)"/>
          <rect x="13" y="18" width="30" height="20" fill="var(--icon-ink)"/>
          <path d="M14 19 L28 30 L42 19" fill="none" stroke="var(--icon-face)" stroke-width="2"/>
          <path d="M14 37 L24 27 M32 27 L42 37" fill="none" stroke="var(--icon-face)" stroke-width="1.5"/>
        </svg>
        <span>Leovalcarce@Mailhub.com</span>
      </div>
    </div>
  </main>
</body>
</html>
```